Daily Deals Website Needs a Landing Page (Home Page will act as the landing page)

We need a landing page for a daily deals website that will act as the home page. We have attached the wire frame and logo for reference. Open to creative ideas and suggestions as long as the main elements of the wireframe are incorporated in the design. Need a very simplistic design approach like Vorplex's search page. (www.vorplex.com) . Very clean and distinct CTA's.

Target Market(s)

Customers looking for deals on everyday use items

Font styles to use
Sans Serif

Requirements
Must have
• clean design, lots of white space and strong CTA .
Nice to have
• need a clean design overall. Strong CTA
Should not have
• Cluttered look. Too many colors, keep it simple

```html
<!DOCTYPE html>
<html lang="en">
<head>
<meta charset="utf-8">
<title>Dealnest – Daily Deals</title>
<link rel="stylesheet" href="https://fonts.googleapis.com/css2?family=Questrial&family=Lato:wght@400;700&display=swap">
<style>
:root{
  --brand-blue:#1f3295;
  --deal-green:#74c863;
  --deal-green-dark:#5fb64d;
  --tab-dark:#222222;
  --ink:#333333;
  --muted:#4a4a4a;
  --white:#ffffff;
}
*{box-sizing:border-box;margin:0;padding:0}
html,body{width:1048px;height:1200px;overflow:hidden;background:var(--white)}
body{position:relative;font-family:"Lato",sans-serif;color:var(--ink)}
.brand{position:absolute;top:38px;left:0;width:100%;display:flex;justify-content:center;align-items:center;gap:12px}
.brand-mark{width:22px;height:22px;background:var(--deal-green)}
.brand-name{font-family:"Questrial",sans-serif;font-size:50px;color:var(--brand-blue);letter-spacing:1px;line-height:1}
.tagline{position:absolute;top:120px;width:100%;text-align:center;font-family:"Questrial",sans-serif;font-size:19px;color:var(--muted);font-weight:700}
.signup-band{position:absolute;left:0;width:100%;height:110px;background:var(--brand-blue)}
.signup-band.top{top:170px}
.signup-band.bottom{top:954px}
.signup-title{position:absolute;left:94px;top:37px;font-family:"Questrial",sans-serif;font-weight:700;font-size:26px;color:var(--white)}
.email-field{position:absolute;left:406px;top:31px;width:393px;height:49px;border-radius:25px;background:var(--white);border:none;padding-left:23px;font-family:"Lato",sans-serif;font-size:13px;color:var(--ink);display:flex;align-items:center}
.btn{display:flex;align-items:center;justify-content:center;border-radius:25px;background:linear-gradient(var(--deal-green),var(--deal-green-dark));color:var(--white);font-family:"Questrial",sans-serif;font-weight:700;font-size:20px;height:49px}
.signup-band .btn{position:absolute;left:807px;top:31px;width:150px}
.deal-card{position:absolute;top:336px;width:448px;height:570px}
.deal-card.featured{left:65px}
.deal-card.promoted{left:538px}
.deal-tab{position:absolute;left:49px;top:0;width:351px;height:58px;background:var(--tab-dark);border-radius:10px 10px 0 0;color:var(--white);font-family:"Questrial",sans-serif;font-weight:700;font-size:23px;display:flex;align-items:center;justify-content:center;letter-spacing:.3px}
.deal-photo{position:absolute;left:0;top:58px;width:448px;height:308px}
.featured .deal-photo{background:linear-gradient(120deg,#6b5038,#c79a68 45%,#e9e4dc 75%,#8a7868)}
.promoted .deal-photo{background:linear-gradient(120deg,#c7ad92,#e6cdb0 45%,#7a5a4a 80%,#5c4238)}
.deal-body{position:absolute;left:21px;top:331px;width:406px;height:239px;background:var(--white);text-align:center}
.deal-title{margin-top:24px;font-family:"Questrial",sans-serif;font-weight:700;font-size:27px;color:var(--brand-blue);letter-spacing:.5px}
.deal-text{margin-top:6px;font-size:14px;line-height:24px;color:var(--ink)}
.deal-body .btn{position:absolute;left:128px;top:182px;width:150px}
.site-footer{position:absolute;top:1093px;width:100%;text-align:center}
.footer-nav{display:flex;justify-content:center;gap:35px;font-weight:700;font-size:14.5px;color:var(--ink);padding-left:8px}
.copyright{margin-top:12px;font-size:14px;color:var(--ink)}
.social{margin-top:12px;display:flex;justify-content:center;gap:18px}
.social span{width:20px;height:20px;border-radius:50%;background:var(--ink)}
</style>
</head>
<body>
<header>
  <div class="brand"><span class="brand-mark"></span><span class="brand-name">Dealnest</span></div>
  <p class="tagline">Excepteur sint occaecat cupidatat non proident</p>
</header>

<section class="signup-band top">
  <h2 class="signup-title">Sign Up For Daily Deals</h2>
  <div class="email-field">Enter Email Address</div>
  <span class="btn">Sign Up</span>
</section>

<article class="deal-card featured">
  <div class="deal-tab">Featured Deal of the Day</div>
  <div class="deal-photo" role="img" aria-label="Clothing store with shirts on mannequins and folded garments"></div>
  <div class="deal-body">
    <h3 class="deal-title">Accusantium Doloremque</h3>
    <p class="deal-text">Nemo enim ipsam voluptatem quia voluptas sit<br>aspernatur aut odit aut fugit, sed quia consequuntur<br>magni dolores eos qui ratione voluptatem<br>sequi nesciunt.</p>
    <span class="btn">Click Here</span>
  </div>
</article>

<article class="deal-card promoted">
  <div class="deal-tab">Promoted Deal of the Day</div>
  <div class="deal-photo" role="img" aria-label="Hands holding an open book over scattered open books"></div>
  <div class="deal-body">
    <h3 class="deal-title">Accusantium Doloremque</h3>
    <p class="deal-text">Nemo enim ipsam voluptatem quia voluptas sit<br>aspernatur aut odit aut fugit, sed quia consequuntur<br>magni dolores eos qui ratione voluptatem<br>sequi nesciunt.</p>
    <span class="btn">Click Here</span>
  </div>
</article>

<section class="signup-band bottom">
  <h2 class="signup-title">Sign Up For Daily Deals</h2>
  <div class="email-field">Enter Email Address</div>
  <span class="btn">Sign Up</span>
</section>

<footer class="site-footer">
  <nav class="footer-nav"><span>Home</span><span>Blog</span><span>Past Daily Deals</span><span>About</span><span>Contact</span><span>Privacy</span></nav>
  <p class="copyright">Copyright © 2021. Company Name.All Right Reserved</p>
  <div class="social" aria-label="Social links"><span></span><span></span><span></span><span></span><span></span></div>
</footer>
</body>
</html>
```